Poster/Handout for a dance

I need a poster designed that can also be made into a hand bill. Id like it to have an elegant feel - maybe black and gold

Wording: (feel free to tweak it)

Founders' Soiree
All adults and invited guests Join us for some R&R
an evening of music, dancing, relaxation, and appetizers and desserts
Friday, February 24 2017
8PM-11PM
North Birch Hall
4817 Maplebrook Cres NW

some ideas of looks below....

Font styles to use
Serif
Script

Colors
757575
000000

Requirements
Must have
• elegance....impact...professionalism
Should not have
• not too casual

```html
<!DOCTYPE html>
<html lang="en">
<head>
<meta charset="utf-8">
<title>Founders' Soiree</title>
<link href="https://fonts.googleapis.com/css2?family=Great+Vibes&family=Cormorant+Garamond:wght@500;600&display=swap" rel="stylesheet">
<style>
  :root {
    --ink: #000000;
    --night: #0c0c0c;
    --smoke: #2b2b2b;
    --ash: #757575;
    --gold: #d8b776;
    --gold-light: #f3dfb0;
    --gold-deep: #a9813f;
    --glow: rgba(255, 226, 160, 0.55);
  }
  * { margin: 0; padding: 0; box-sizing: border-box; }
  html, body {
    width: 894px;
    height: 1200px;
    overflow: hidden;
    background: var(--ink);
  }
  .poster {
    position: relative;
    width: 894px;
    height: 1200px;
    overflow: hidden;
    background:
      radial-gradient(ellipse 60% 45% at 50% 50%, var(--smoke) 0%, var(--night) 70%, var(--ink) 100%);
    color: var(--gold);
    font-family: "Cormorant Garamond", Georgia, serif;
    text-align: center;
  }
  .string-lights {
    position: absolute;
    left: 0;
    top: 0;
    width: 894px;
    height: 640px;
    background:
      radial-gradient(ellipse 70% 22% at 50% 18%, var(--glow) 0%, rgba(255,226,160,0.18) 55%, transparent 100%),
      radial-gradient(ellipse 12% 55% at 6% 45%, rgba(255,226,160,0.28) 0%, transparent 100%),
      radial-gradient(ellipse 12% 50% at 95% 45%, rgba(255,226,160,0.28) 0%, transparent 100%),
      linear-gradient(180deg, rgba(60,48,28,0.6) 0%, transparent 60%);
  }
  .title {
    position: absolute;
    left: 0;
    width: 100%;
    font-family: "Great Vibes", cursive;
    font-weight: 400;
    line-height: 1;
    background: linear-gradient(180deg, var(--gold-light) 0%, var(--gold) 55%, var(--gold-deep) 100%);
    -webkit-background-clip: text;
    background-clip: text;
    color: transparent;
  }
  .title-first { top: 295px; font-size: 140px; padding-right: 40px; }
  .title-second { top: 455px; font-size: 140px; padding-left: 130px; }
  .invitation {
    position: absolute;
    left: 0;
    top: 642px;
    width: 100%;
    font-size: 33px;
    font-weight: 500;
    line-height: 54px;
    letter-spacing: 0.5px;
  }
  .invitation .caps { text-transform: uppercase; letter-spacing: 1px; }
  .flourish {
    position: absolute;
    left: 397px;
    top: 880px;
    width: 100px;
    height: 56px;
    border-radius: 50%;
    background: radial-gradient(ellipse at center, rgba(216,183,118,0.45) 0%, transparent 70%);
  }
  .event-details {
    position: absolute;
    left: 0;
    top: 962px;
    width: 100%;
    font-size: 27px;
    font-weight: 500;
    line-height: 41.5px;
    text-transform: uppercase;
    letter-spacing: 1px;
  }
</style>
</head>
<body>
  <main class="poster">
    <div class="string-lights" role="img" aria-label="Glowing gold strings of lights and hanging bulbs draped across the top and sides"></div>

    <h1>
      <span class="title title-first">Founders'</span>
      <span class="title title-second">Soiree</span>
    </h1>

    <p class="invitation">
      All adults and invited guests<br>
      <span class="caps">Join us for some R&amp;R</span><br>
      an evening of music, dancing, relaxation,<br>
      and appetizers and desserts
    </p>

    <div class="flourish" role="img" aria-label="Small gold scroll ornament"></div>

    <p class="event-details">
      Friday, February 24 2017<br>
      8PM-11PM<br>
      North Birch Hall<br>
      4817 Maplebrook Cres NW
    </p>
  </main>
</body>
</html>
```